We sell companies excess stock for them

We need a business card for a company based in New Zealand called 'StockHarbor'.

Check out our website to get an idea www.stockharbor.example

We help other businesses to;
- Sell Excess Stock
- Manage Product Returns
- Sell Company Assets

Our logo is attached for your reference
The font used is 'RifficFree-Bold'

Target Market(s)

Businesses

Industry/Entity Type

Business

Contact Information for Business Card

Name: Mark Pellow
Phone: 027 846 2093
email: markpellow@stockharbor.example
website: www.stockharbor.example

Font styles to use
Other font styles liked:
• Unsure

Colors
9bcb3b

Requirements
Must have
• coming soon
Nice to have
• coming soon
Should not have
• coming soon

```html
<!DOCTYPE html>
<html lang="en">
<head>
<meta charset="utf-8">
<title>StockHarbor – Business Card</title>
<link rel="stylesheet" href="https://fonts.googleapis.com/css2?family=Source+Sans+3:wght@400;600;700&display=swap">
<style>
  :root {
    --card-bg: #ffffff;
    --ink: #111111;
    --brand-green: #9bcb3b;
    --divider: #111111;
  }
  html, body {
    margin: 0;
    padding: 0;
    width: 1200px;
    height: 737px;
    overflow: hidden;
    background: var(--card-bg);
  }
  .business-card {
    position: relative;
    width: 1200px;
    height: 737px;
    background: var(--card-bg);
    font-family: "Source Sans 3", "Myriad Pro", Arial, sans-serif;
    color: var(--ink);
  }
  .brand-mark {
    position: absolute;
    top: 78px;
    right: 57px;
    display: flex;
    align-items: center;
    gap: 16px;
  }
  .brand-mark__dot {
    width: 50px;
    height: 50px;
    border-radius: 50%;
    background: var(--brand-green);
  }
  .brand-mark__name {
    font-size: 52px;
    font-weight: 700;
    line-height: 1;
    color: var(--brand-green);
  }
  .identity {
    position: absolute;
    right: 688px;
    top: 339px;
    text-align: right;
  }
  .identity__name {
    margin: 0;
    font-size: 88px;
    line-height: 1;
    letter-spacing: -1px;
    white-space: nowrap;
  }
  .identity__first {
    font-weight: 700;
  }
  .identity__last {
    font-weight: 400;
  }
  .identity__phone {
    margin: -4px 0 0;
    font-size: 38px;
    line-height: 1;
    font-weight: 400;
    white-space: nowrap;
  }
  .divider {
    position: absolute;
    left: 602px;
    top: 212px;
    width: 6px;
    height: 396px;
    background: var(--divider);
  }
  .contact-list {
    position: absolute;
    left: 670px;
    top: 365px;
    margin: 0;
    padding: 0;
    list-style: none;
    font-size: 27px;
    font-weight: 600;
    line-height: 40px;
    white-space: nowrap;
  }
</style>
</head>
<body>
  <main class="business-card">
    <div class="brand-mark">
      <span class="brand-mark__dot" aria-hidden="true"></span>
      <span class="brand-mark__name">StockHarbor</span>
    </div>

    <section class="identity">
      <h1 class="identity__name"><span class="identity__first">Mark</span> <span class="identity__last">Pellow</span></h1>
      <p class="identity__phone">027 846 2093</p>
    </section>

    <div class="divider" aria-hidden="true"></div>

    <ul class="contact-list">
      <li class="contact-list__email">email : markpellow@stockharbor.example</li>
      <li class="contact-list__web">website : www.stockharbor.example</li>
    </ul>
  </main>
</body>
</html>
```